Gift voucher for a photo shoot, folding card DIN long (21 x 9.8 cm)

Hello, I'm a professional photographer and need a new design for my gift voucher card for a photo shoot. The design should be applicable to all types of photo shoots (neutral). I prefer a sophisticated design. The folded card should be printed on both sides.
My data should be included: Logo, Address: Wendtholzer Strße 27, 07549 Gera, Email: fotograf@malteburgardt.eu, Website: www.malteburgardt.eu Tel.: 0173 / 4958302
Updates

Please design the folding card in DIN long format (105 x 210 mm, landscape format). The card should open horizontally. Please design the front with the words "Gift voucher for you" and my logo. Please make the logo small – the words "Gift voucher" should be in the foreground.
The colors - use elegant gray with gold or white font color.
The inside should contain the words: Photo shoot for ........ worth .....€, as well as my logo.
My contact details should be on the back.

Target Market(s)

Private customer

Colors

Designer to choose only greyscale colors for use in the design.

Requirements
Must have
• Noble appearance, a gift voucher that one likes to give away, words: Gift voucher for you, photo shoot for ..., worth .......€
Nice to have
• Noble appearance of the gift voucher, a gift voucher that you like to give away
Should not have
• no pictures

```html
<!DOCTYPE html>
<html lang="de">
<head>
<meta charset="utf-8">
<title>Geschenkgutschein – Malte Burgardt Fotograf</title>
<link href="https://fonts.googleapis.com/css2?family=Montserrat:wght@300;400;500;700&display=swap" rel="stylesheet">
<style>
  :root {
    --stage: #e4e4e4;
    --card: #8c8d8b;
    --card-shade: #7b7c7b;
    --fold: rgba(0, 0, 0, 0.12);
    --white: #ffffff;
    --gold: #d9c89a;
    --gold-deep: #b9a470;
  }
  * { box-sizing: border-box; margin: 0; padding: 0; }
  html, body {
    width: 1200px; height: 742px; overflow: hidden;
    background: var(--stage);
    font-family: "Montserrat", sans-serif;
    color: var(--white);
  }
  .sheet {
    position: absolute; left: 40px; width: 1120px; height: 280px;
    display: flex;
    box-shadow: 0 6px 18px rgba(0, 0, 0, 0.18);
  }
  .sheet--outside { top: 71px; }
  .sheet--inside { top: 391px; }
  .panel {
    position: relative; width: 560px; height: 280px;
    background: var(--card); overflow: hidden;
  }
  .panel + .panel { border-left: 1px solid var(--fold); }

  .camera-art {
    position: absolute; left: 0; top: 82px; width: 250px; height: 198px;
    background: linear-gradient(160deg, var(--card-shade), #757675);
    border-top-right-radius: 18px;
  }

  .gold { color: var(--gold); background: linear-gradient(90deg, var(--gold), #efe3c0 50%, var(--gold-deep)); -webkit-background-clip: text; background-clip: text; -webkit-text-fill-color: transparent; }

  .headline {
    position: absolute; right: 38px; top: 26px; text-align: right;
    font-weight: 300; line-height: 1;
  }
  .headline .word-small { font-size: 32px; }
  .headline .word-big { font-size: 42px; font-weight: 400; }
  .headline .line-two { display: block; margin-top: 6px; }

  .rule {
    position: absolute; right: 38px; height: 1px;
    background: linear-gradient(90deg, transparent, var(--white));
  }

  .brand {
    position: absolute; display: flex; align-items: center; gap: 8px;
    font-weight: 400; color: var(--white); white-space: nowrap;
  }
  .brand__dot {
    border: 1.5px solid var(--white); border-radius: 50%;
  }
  .brand--small { right: 38px; top: 200px; font-size: 17px; }
  .brand--small .brand__dot { width: 22px; height: 22px; }
  .brand--large { left: 0; right: 0; top: 70px; justify-content: center; font-size: 30px; gap: 12px; }
  .brand--large .brand__dot { width: 38px; height: 38px; }

  .contact {
    position: absolute; left: 34px; right: 34px; top: 196px;
    display: flex; align-items: center; gap: 18px; font-size: 16px; font-weight: 400;
  }
  .contact__phone strong { font-weight: 700; }
  .contact__divider { width: 1px; height: 46px; background: var(--white); }
  .contact__web { line-height: 1.55; }

  .services {
    position: absolute; left: 38px; top: 44px; list-style: none;
    font-size: 18px; font-weight: 400; line-height: 40px;
  }

  .offer-title {
    position: absolute; right: 32px; top: 18px;
    font-size: 42px; font-weight: 500; line-height: 1;
  }
  .offer-for {
    position: absolute; left: 350px; top: 80px; font-size: 30px; font-weight: 300;
  }
  .field {
    position: absolute; font-size: 17px; font-weight: 400; display: flex; align-items: flex-end;
  }
  .field__blank { display: inline-block; border-bottom: 1px solid var(--white); }
  .field--value { right: 34px; top: 192px; }
  .field--value .field__blank { width: 150px; margin-left: 2px; height: 18px; }
  .field--number { left: 460px; top: 232px; }
</style>
</head>
<body>

<section class="sheet sheet--outside" aria-label="Außenseite">
  <article class="panel panel--back">
    <div class="brand brand--large">
      <span class="brand__dot"></span>
      <span class="brand__name">Malte Burgardt</span>
    </div>
    <div class="contact">
      <p class="contact__phone">Tel: <strong>0173 / 4958302</strong></p>
      <span class="contact__divider"></span>
      <p class="contact__web">fotograf@malteburgardt.eu<br>www.malteburgardt.eu</p>
    </div>
  </article>

  <article class="panel panel--front">
    <div class="camera-art" role="img" aria-label="Faint camera illustration in dark grey"></div>
    <h1 class="headline">
      <span class="word-small">Geschenk</span> <span class="word-big gold">Gutschein</span>
      <span class="line-two"><span class="word-small">für</span> <span class="word-big">Dich</span></span>
    </h1>
    <span class="rule" style="top:153px; width:250px;"></span>
    <div class="brand brand--small">
      <span class="brand__dot"></span>
      <span class="brand__name">Malte Burgardt</span>
    </div>
  </article>
</section>

<section class="sheet sheet--inside" aria-label="Innenseite">
  <article class="panel panel--services">
    <ul class="services">
      <li>Familie</li>
      <li>Hochzeit</li>
      <li>Portrait</li>
      <li>Business</li>
      <li>Karriere</li>
    </ul>
  </article>

  <article class="panel panel--voucher">
    <div class="camera-art" role="img" aria-label="Faint camera illustration in dark grey"></div>
    <h2 class="offer-title gold">Fotoshooting</h2>
    <p class="offer-for">für</p>
    <span class="rule" style="top:129px; width:240px;"></span>
    <p class="field field--value">im Wert von<span class="field__blank"></span>€</p>
    <p class="field field--number">Nr:</p>
  </article>
</section>

</body>
</html>
```